Important Solar Energy Company Needs a Stationery Design

I need a modern, attractive, corporate stationary design (letter head and business card)
Attached Company Logo

Target Market(s)

Upmarket

Industry/Entity Type

Business

Colors
ec1f27
ffffff
757575
cbcbcb
000000

```html
<!DOCTYPE html>
<html lang="en">
<head>
<meta charset="utf-8">
<title>Solvanta Business Card</title>
<link rel="stylesheet" href="https://fonts.googleapis.com/css2?family=Didact+Gothic&family=Montserrat:wght@600;700&display=swap">
<style>
  :root {
    --brand-red: #ec1f27;
    --deep-red: #a8151b;
    --white: #ffffff;
    --grey: #757575;
    --light-grey: #cbcbcb;
    --black: #000000;
    --ink: #333333;
    --backdrop: #2e2e2e;
  }
  * { margin: 0; padding: 0; box-sizing: border-box; }
  html, body { width: 1200px; height: 768px; overflow: hidden; }
  body {
    background: var(--backdrop);
    font-family: "Didact Gothic", "Century Gothic", sans-serif;
    position: relative;
  }
  .card {
    position: absolute;
    top: 234px;
    width: 520px;
    height: 300px;
    border-radius: 18px;
    overflow: hidden;
  }
  .card-back {
    left: 50px;
    background: linear-gradient(120deg, var(--brand-red) 0%, #c81a21 55%, var(--deep-red) 100%);
    display: flex;
    align-items: center;
    justify-content: center;
  }
  .back-mark {
    display: flex;
    flex-direction: column;
    align-items: center;
    gap: 14px;
  }
  .back-circle {
    width: 120px;
    height: 120px;
    border-radius: 50%;
    background: #d4d4d4;
  }
  .back-name {
    color: var(--white);
    font-family: "Montserrat", sans-serif;
    font-weight: 600;
    font-size: 22px;
    letter-spacing: 3px;
  }
  .card-front {
    left: 630px;
    background: linear-gradient(160deg, var(--white) 40%, #e9e9e9 100%);
  }
  .brand {
    position: absolute;
    left: 34px;
    top: 34px;
    display: flex;
    align-items: center;
    gap: 12px;
  }
  .brand-circle {
    width: 54px;
    height: 54px;
    border-radius: 50%;
    background: var(--brand-red);
  }
  .brand-name {
    font-family: "Montserrat", sans-serif;
    font-weight: 600;
    font-size: 22px;
    letter-spacing: 3px;
    color: var(--ink);
  }
  .divider {
    position: absolute;
    left: 34px;
    top: 136px;
    width: 322px;
    height: 1px;
    background: var(--brand-red);
  }
  .contact-list {
    position: absolute;
    left: 34px;
    top: 148px;
    list-style: none;
    font-size: 13px;
    color: var(--grey);
    line-height: 20px;
  }
  .contact-list li { display: flex; align-items: center; gap: 8px; }
  .contact-list svg { width: 12px; height: 12px; fill: var(--brand-red); flex: none; }
  .person {
    position: absolute;
    left: 364px;
    top: 112px;
    white-space: nowrap;
  }
  .person-name {
    font-family: "Montserrat", sans-serif;
    font-weight: 700;
    font-size: 17px;
    line-height: 22px;
    color: var(--brand-red);
  }
  .person-title { font-size: 14px; line-height: 20px; color: var(--ink); }
  .person-tab {
    position: absolute;
    right: 0;
    top: 124px;
    width: 8px;
    height: 30px;
    background: var(--brand-red);
  }
  .address {
    position: absolute;
    right: 40px;
    top: 200px;
    text-align: right;
    font-size: 14px;
    line-height: 19px;
    font-style: normal;
    color: var(--grey);
  }
  .base-band {
    position: absolute;
    left: 0;
    bottom: 0;
    width: 100%;
    height: 12px;
    display: flex;
  }
  .base-band .band-red { flex: 0 0 66%; background: var(--brand-red); }
  .base-band .band-black { flex: 1; background: var(--black); }
</style>
</head>
<body>
  <section class="card card-back" aria-label="Card back">
    <div class="back-mark">
      <div class="back-circle"></div>
      <span class="back-name">SOLVANTA</span>
    </div>
  </section>

  <section class="card card-front" aria-label="Card front">
    <div class="brand">
      <div class="brand-circle"></div>
      <span class="brand-name">SOLVANTA</span>
    </div>
    <div class="divider"></div>

    <ul class="contact-list">
      <li><svg viewBox="0 0 12 12"><path d="M2 0h3l1 3-2 1.5a7 7 0 0 0 3.5 3.5L9 6l3 1v3a2 2 0 0 1-2 2A10 10 0 0 1 0 2a2 2 0 0 1 2-2z"/></svg>555 210 4471</li>
      <li><svg viewBox="0 0 12 12"><path d="M3 0h6a1 1 0 0 1 1 1v10a1 1 0 0 1-1 1H3a1 1 0 0 1-1-1V1a1 1 0 0 1 1-1zm0 1.5v7.5h6V1.5z"/></svg>555 318 9026</li>
      <li><svg viewBox="0 0 12 12"><path d="M3 0h6v3H3zM0 4h12v5h-2v3H2V9H0zm3 3v4h6V7z"/></svg>555 702 6185</li>
      <li><svg viewBox="0 0 12 12"><path d="M0 2h12v8H0zm1 1l5 3.5L11 3z"/></svg>info@solvanta.com</li>
    </ul>

    <div class="person">
      <div class="person-name">Marco Delgado</div>
      <div class="person-title">CEO/Founder</div>
    </div>
    <div class="person-tab"></div>

    <address class="address">
      1420 Harbor Ridge Road<br>
      Tucson, Arizona 85701<br>
      www.solvanta.com
    </address>

    <div class="base-band">
      <div class="band-red"></div>
      <div class="band-black"></div>
    </div>
  </section>
</body>
</html>
```